Not your average candle company needs label design

MOSS + RUIN A Brand Deck for Disruptive Candles
WHO WE ARE
Moss + Ruin is a disruptive candle brand built on contrast. We create clean-burning, scent-forward rituals for people who are both grounded and undone.
We’re not here for the beige wellness aesthetic. We’re here for the moments that are messy, bold, emotional, and beautifully real.
Rooted in botanical craftsmanship. Branded in poetic defiance.
WHAT WE WANT PEOPLE TO THINK
When someone encounters Moss + Ruin, we want them to feel like they’ve stumbled into something intimate, moody, and unforgettable.
We want them to think:
• “This brand gets me.”
• “This feels like design, emotion, and scent in one.”
• “It’s art I can burn.”
• “I’ve never seen a candle brand like this before.”
Our name alone sparks curiosity. Our story keeps them. Our product delivers.

Target Market(s)

Women and men ages 25–45 who appreciate thoughtful design and emotional storytelling People who love brands like Farvale, Kid Whiffs, Pelican Grange, Mivune, and Du Vanto Design-minded buyers who shop indie, high-end, or artisanal and care about self-expression through scent Emotionally intelligent rebels. Introspective, edgy, but craving grounding rituals.

Industry/Entity Type

Candle Industry

Font styles to use
Other font styles liked:
• Moss should be more refined in a serif font and I like mistrully font for ruin.

Requirements
Must have
• Space for scent name and optionally, a small poetic tagline (like Still Riot. Low Flame.) Layout that’s elegant but with tension — surprise us with something that doesn't play it safe Optional: room for batch no., burn time, scent notes on side or bottom. MOSS + RUIN Still Riot. Low Flame. Scent name example: Lanternfall A silent vow to stay grounded. Earthy and grounding — like old books, soft shadows, and the quiet certainty of knowing who you are. [optional: 7 oz / 198g | coconut soy wax | 45+ hr burn time]
Nice to have
• raw edge opening with gold font. Open to colored labels. We’re creating an unforgettable candle brand called Moss + Ruin — a contrast-rich, emotionally resonant collection of candles that blend botanical beauty with bold edge. The name is intentional: Moss reflects grounding, ritual, and plant-based purity; Ruin speaks to vulnerability, chaos, and strength through contrast. Our brand is not dark or gothic — it’s confident, elevated, and style-forward, with packaging that feels like a cross between modern apothecary and high fashion. Think Mivune meets Dale Pruitt. Gloss vessels, textured labels, contrasting fonts, and emotional scent storytelling.
Should not have
• goth vibe, typical candle label template layout.

```html
<!DOCTYPE html>
<html lang="en">
<head>
<meta charset="UTF-8">
<title>Moss + Ruin — Lanternfall Label</title>
<link rel="stylesheet" href="https://fonts.googleapis.com/css2?family=Playfair+Display:wght@700&family=Montserrat:ital,wght@0,400;0,500;0,600;1,500&display=swap">
<style>
  :root {
    --backdrop: #eceef0;
    --label-gold: #b3a274;
    --ink: #111111;
    --paper: #ffffff;
  }
  * { margin: 0; padding: 0; box-sizing: border-box; }
  html, body {
    width: 1200px;
    height: 800px;
    overflow: hidden;
    background: var(--backdrop);
  }
  .canvas {
    position: relative;
    width: 1200px;
    height: 800px;
    background: var(--backdrop);
  }
  .label {
    position: absolute;
    left: 240px;
    top: 155px;
    width: 720px;
    height: 490px;
    background: var(--label-gold);
    color: var(--ink);
  }
  .brand-row {
    position: absolute;
    left: 0;
    top: 66px;
    width: 720px;
    display: flex;
    justify-content: center;
    align-items: center;
    gap: 18px;
  }
  .brand-name {
    font-family: "Playfair Display", serif;
    font-weight: 700;
    font-size: 58px;
    letter-spacing: 2px;
    line-height: 1;
  }
  .brand-mark {
    width: 14px;
    height: 14px;
    background: var(--ink);
  }
  .collection-bar {
    position: absolute;
    left: 0;
    top: 160px;
    width: 260px;
    height: 40px;
    background: var(--ink);
    color: var(--paper);
    font-family: "Montserrat", sans-serif;
    font-weight: 400;
    font-size: 20px;
    line-height: 40px;
    padding-left: 22px;
    letter-spacing: 2px;
  }
  .tagline {
    position: absolute;
    left: 290px;
    top: 168px;
    font-family: "Montserrat", sans-serif;
    font-style: italic;
    font-weight: 500;
    font-size: 20px;
    letter-spacing: 1px;
    line-height: 24px;
  }
  .scent-block {
    position: absolute;
    left: 70px;
    top: 240px;
    width: 420px;
    text-align: center;
  }
  .scent-name {
    font-family: "Playfair Display", serif;
    font-weight: 700;
    font-size: 40px;
    letter-spacing: 1px;
    line-height: 1.1;
  }
  .scent-tagline {
    font-family: "Montserrat", sans-serif;
    font-style: italic;
    font-weight: 500;
    font-size: 19px;
    margin-top: 6px;
  }
  .wax-type {
    display: inline-block;
    margin-top: 14px;
    border: 2px solid var(--ink);
    padding: 3px 16px;
    font-family: "Montserrat", sans-serif;
    font-weight: 400;
    font-size: 18px;
    letter-spacing: 0.5px;
  }
  .net-weight {
    margin-top: 24px;
    font-family: "Montserrat", sans-serif;
    font-weight: 500;
    font-size: 19px;
  }
  .burn-time {
    position: absolute;
    left: 530px;
    top: 262px;
    width: 130px;
    border-top: 2px solid var(--ink);
    border-bottom: 2px solid var(--ink);
    padding: 10px 0;
    text-align: center;
    font-family: "Montserrat", sans-serif;
  }
  .burn-hours {
    font-weight: 600;
    font-size: 30px;
    line-height: 1.1;
  }
  .burn-caption {
    font-weight: 500;
    font-size: 12px;
    letter-spacing: 2px;
    margin-top: 4px;
  }
</style>
</head>
<body>
<main class="canvas">
  <section class="label">
    <div class="brand-row">
      <h1 class="brand-name">MOSS + RUIN</h1>
      <span class="brand-mark" aria-hidden="true"></span>
    </div>
    <div class="collection-bar">STILL RIOT</div>
    <p class="tagline">low flame.</p>

    <div class="scent-block">
      <h2 class="scent-name">LANTERNFALL</h2>
      <p class="scent-tagline">a silent vow to stay grounded</p>
      <p class="wax-type">COCONUT SOY WAX</p>
      <p class="net-weight">7oz - 198g</p>
    </div>

    <div class="burn-time">
      <p class="burn-hours">45+ HR</p>
      <p class="burn-caption">BURN TIME</p>
    </div>
  </section>
</main>
</body>
</html>
```